Business Card Design

We offer full auto repair and auto customization from custom wheels to lift kits and drop kits we do it all. I want something that grabs your attention from the start but nothing flashy i am more of a clean crisp modern kinda of guy. I plan on using the design on my business cards and my main business sign .
Updates
I have up loaded an image of my currant business card designed by me , I would like to improve on it
Target Market(s)
20-35 male and female
Industry/Entity Type
Business
Contact Information for Business Card
Calloway Tire Service
48306 1/2 Pruett rd
Houston TX, 77391
Manager: Gavin Alcott
P:832-555-0147
F:832-555-0182
Email:Gavin@callowayautoandtire.example
website:Callowayautoandtire.example
Look and feel

```html
<!DOCTYPE html>
<html lang="en">
<head>
<meta charset="utf-8">
<title>Calloway Tire Service – Business Card</title>
<link rel="stylesheet" href="https://fonts.googleapis.com/css2?family=Open+Sans:wght@400;600&display=swap">
<style>
  :root {
    --brand-blue: #0f4f9e;
    --name-blue: #1c44a0;
    --navy: #2a2566;
    --text-grey: #6b6b6b;
    --paper: #ffffff;
    --page: #ffffff;
  }
  * { margin: 0; padding: 0; box-sizing: border-box; }
  html, body {
    width: 1200px;
    height: 1000px;
    overflow: hidden;
    background: var(--page);
    font-family: "Open Sans", Arial, sans-serif;
  }
  .card {
    position: absolute;
    left: 248px;
    width: 747px;
    height: 437px;
    background: var(--paper);
    box-shadow: 1px 2px 5px rgba(0,0,0,0.35);
    overflow: hidden;
  }
  .card--front { top: 35px; }
  .card--back { top: 527px; height: 436px; }
  .card svg.bands { position: absolute; left: 0; top: 0; }
  .bands polygon, .bands rect { fill: var(--brand-blue); }

  .front-brand {
    position: absolute;
    left: 0; right: 0; top: 178px;
    display: flex;
    align-items: center;
    justify-content: center;
    gap: 22px;
  }
  .front-brand__mark {
    width: 70px; height: 70px;
    background: var(--brand-blue);
  }
  .front-brand__name {
    color: var(--navy);
    font-weight: 600;
    font-size: 38px;
    line-height: 1.05;
    letter-spacing: 2px;
    text-transform: uppercase;
  }

  .back-brand {
    position: absolute;
    left: 0; width: 724px; top: 67px;
    text-align: center;
  }
  .back-brand__mark {
    width: 42px; height: 42px;
    margin: 0 auto 14px;
    background: var(--brand-blue);
  }
  .back-brand__name {
    color: var(--name-blue);
    font-size: 27px;
    line-height: 34px;
  }
  .back-brand__address {
    color: var(--text-grey);
    font-size: 19px;
    line-height: 26px;
  }
  .person {
    position: absolute;
    left: 44px; top: 210px;
  }
  .person__name {
    color: var(--name-blue);
    font-size: 27px;
    line-height: 32px;
  }
  .person__role {
    color: var(--text-grey);
    font-size: 19px;
    line-height: 22px;
  }
  .contact-list {
    position: absolute;
    left: 44px; top: 286px;
    list-style: none;
  }
  .contact-list li {
    display: flex;
    align-items: center;
    height: 31px;
    color: var(--text-grey);
    font-size: 16.5px;
  }
  .contact-list svg {
    width: 22px; height: 22px;
    margin-right: 14px;
    fill: var(--name-blue);
  }
</style>
</head>
<body>

<section class="card card--front" aria-label="Card front">
  <svg class="bands" width="747" height="437" viewBox="248 35 747 437" aria-hidden="true">
    <polygon points="248,35 270,35 248,68"/>
    <polygon points="305,35 395,35 350,104 258,104"/>
    <polygon points="440,35 505,35 460,104 395,104"/>
    <polygon points="545,35 680,35 635,104 490,104"/>
    <polygon points="715,35 995,35 950,104 668,104"/>
    <polygon points="248,472 272,472 316,404 292,404"/>
    <polygon points="305,472 368,472 410,404 347,404"/>
    <polygon points="400,472 510,472 552,404 442,404"/>
    <polygon points="545,472 685,472 728,404 588,404"/>
    <polygon points="718,472 995,472 995,404 760,404"/>
  </svg>
  <div class="front-brand">
    <div class="front-brand__mark"></div>
    <div class="front-brand__name">Calloway Tire<br>Service</div>
  </div>
</section>

<section class="card card--back" aria-label="Card back">
  <svg class="bands" width="747" height="436" viewBox="248 527 747 436" aria-hidden="true">
    <rect x="927" y="527" width="68" height="436"/>
    <polygon points="927,527 945,527 995,556 995,600 927,560" fill="#fff" style="fill:#fff"/>
    <polygon points="927,703 995,747 995,780 927,736" style="fill:#fff"/>
  </svg>

  <div class="back-brand">
    <div class="back-brand__mark"></div>
    <div class="back-brand__name">Calloway Tire Service</div>
    <div class="back-brand__address">48306 1/2 Pruett rd Houston TX, 77391</div>
  </div>

  <div class="person">
    <div class="person__name">Gavin Alcott</div>
    <div class="person__role">Manager</div>
  </div>

  <ul class="contact-list">
    <li>
      <svg viewBox="0 0 24 24" aria-hidden="true"><path d="M7 1h10a2 2 0 0 1 2 2v18a2 2 0 0 1-2 2H7a2 2 0 0 1-2-2V3a2 2 0 0 1 2-2zm0 3v14h10V4H7zm5 15.5a1.2 1.2 0 1 0 0 2.4 1.2 1.2 0 0 0 0-2.4z"/></svg>
      832-555-0147
    </li>
    <li>
      <svg viewBox="0 0 24 24" aria-hidden="true"><path d="M2 7h4v15H2zM7 9h15v13H7zM10 2h9v6h-9zM9 12h3v2H9zm5 0h3v2h-3zm5 0h2v2h-2zM9 16h3v2H9zm5 0h3v2h-3zm5 0h2v2h-2z"/></svg>
      832-555-0182
    </li>
    <li>
      <svg viewBox="0 0 24 24" aria-hidden="true"><path d="M1 5h22v2l-11 7L1 7zm0 4l11 7 11-7v10H1z"/></svg>
      Gavin@callowayautoandtire.example
    </li>
    <li>
      <svg viewBox="0 0 24 24" aria-hidden="true"><path d="M12 2a10 10 0 1 0 0 20 10 10 0 0 0 0-20zm0 1.6c1.3 1.2 2.3 3.4 2.6 6.4H9.4c.3-3 1.3-5.2 2.6-6.4zM8.2 4.4A13 13 0 0 0 7.8 10H3.7a8.4 8.4 0 0 1 4.5-5.6zm7.6 0A8.4 8.4 0 0 1 20.3 10h-4.1a13 13 0 0 0-.4-5.6zM3.7 11.6h4.1a13 13 0 0 0 .4 5.6 8.4 8.4 0 0 1-4.5-5.6zm5.7 0h5.2c-.3 3-1.3 5.2-2.6 6.4-1.3-1.2-2.3-3.4-2.6-6.4zm6.8 0h4.1a8.4 8.4 0 0 1-4.5 5.6 13 13 0 0 0 .4-5.6z"/></svg>
      Callowayautoandtire.example
    </li>
  </ul>
</section>

</body>
</html>
```